Webdesign für islamisches Bestattungsunternehmen
Sehr flexibel, sehr schnell in der Umsetzung als auch der Änderung! Wir werden ihn auf jeden Fall nochmal buchen sobald wir ein neues Projekt haben!
Zielgruppe
islamisches Bestattungsunternehmen, Grabsteine, Grabpflege
Aufgabenstellung
wir wollen ein elegantes design mit einem hauch an exklusivität. wir sind nicht auf billig aus, tatsächlich hochwertig, etwas teurer als die konkurrenz aber dafür bieten wir auch was an.
unser logo haben wir auch hier machen lassen.
www.nurelan-bestattung.eu
LEUTE!
Wir wünschen uns dass direkt auf der ersten seite die 3 optionen sofort ersichtlich sind!!! nicht dass die leute noch runterscrollen müssen...

```html
<!DOCTYPE html>
<html lang="de">
<head>
<meta charset="utf-8">
<title>Nurelan-Bestattung – Bestattungen deutschlandweit</title>
<link rel="stylesheet" href="https://fonts.googleapis.com/css2?family=Cinzel:wght@400;600;700&family=Cinzel+Decorative:wght@700&family=Mukta:wght@300;400&family=Cormorant+Garamond:ital,wght@0,500;1,400&display=swap">
<style>
:root{
  --bg:#000;
  --gold:#f0d6a4;
  --gold-soft:#d9c08f;
  --cream:#efd7aa;
  --button:#efdf8e;
  --button-text:#2a2310;
  --card:#050505;
  --card-bar:#3a3a3a;
  --footer:#1c1b1e;
  --muted:#cfc6b5;
  --line:#5a4e38;
}
*{margin:0;padding:0;box-sizing:border-box}
html,body{width:1200px;height:2552px;overflow:hidden;background:var(--bg)}
body{position:relative;font-family:"Mukta",sans-serif;color:var(--gold)}
.abs{position:absolute}
.center{left:0;width:1200px;text-align:center}
.topbar{top:13px;font-size:8px;color:#e8e0d0;display:flex;align-items:center;gap:5px}
.topbar svg{width:9px;height:9px}
.brand{left:500px;top:32px;width:200px;text-align:center;font-family:"Cinzel",serif;font-weight:600;font-size:12px;color:var(--gold);letter-spacing:.5px}
.brand-dot{display:inline-block;width:6px;height:6px;border-radius:50%;background:var(--gold);margin-right:5px;vertical-align:1px}
.nav{top:70px;left:0;width:1200px;display:flex;justify-content:center;gap:40px;font-size:9px;letter-spacing:.4px;color:#e8e0d0}
.nav a{color:inherit;text-decoration:none;padding-bottom:4px}
.nav a.active{border-bottom:1px solid var(--gold)}
.frame{left:0;top:0}
.hero-photo{left:160px;top:110px;width:880px;height:440px;border-radius:70px 70px 0 0;
  background:radial-gradient(ellipse at 50% 40%,#6b4c3e 0%,#4a2b25 35%,#2a1412 65%,#000 100%)}
.hero-title{top:178px;font-family:"Cinzel Decorative",serif;font-weight:700;font-size:31px;line-height:40px;color:var(--gold);letter-spacing:.5px}
.hero-title .gap{display:block;height:10px}
.btn{display:flex;align-items:center;justify-content:center;background:var(--button);color:var(--button-text);
  font-family:"Cinzel",serif;font-weight:700;font-size:10px;text-decoration:none}
.btn-outline{display:flex;align-items:center;justify-content:center;border:1px solid #c9c0ae;color:#e8e0d0;
  font-family:"Cinzel",serif;font-size:10px;text-decoration:none}
.service-card{top:415px;width:204px;height:125px;background:var(--card)}
.service-card h3{position:absolute;left:21px;top:22px;font-family:"Cinzel",serif;font-weight:400;font-size:17px;line-height:23px;color:var(--gold)}
.service-card .bar{position:absolute;left:0;bottom:0;width:100%;height:40px;background:var(--card-bar);
  font-family:"Cinzel",serif;font-size:11px;color:var(--gold);padding:14px 0 0 24px}
.service-card .art{position:absolute;right:0;bottom:0;width:66px;height:84px;background:var(--cream);border-radius:12px 12px 0 0;opacity:.92}
.about-title{left:264px;top:655px;font-family:"Cinzel",serif;font-size:21px;line-height:27px;color:var(--gold)}
.about-text{left:264px;top:756px;width:240px;font-size:9.5px;line-height:15px;color:#eee}
.hours{left:264px;font-family:"Cormorant Garamond",serif;font-weight:500;font-size:11px;color:#eee}
.photo-arch{left:732px;top:641px;width:188px;height:252px;background:linear-gradient(160deg,#7a3a1e,#c47f33 40%,#f3d88a 70%,#f7ecc0)}
.photo-people{left:601px;top:705px;width:210px;height:237px;background:linear-gradient(135deg,#3a342b,#151310 60%,#050505)}
.eyebrow{font-family:"Cinzel",serif;font-size:10px;letter-spacing:2.5px;color:var(--gold-soft)}
.section-title{font-family:"Cinzel",serif;font-size:21px;color:var(--gold)}
.quote{top:1107px;font-family:"Cormorant Garamond",serif;font-style:italic;font-size:12.5px;line-height:22.5px;color:#eee}
.product-img{top:1390px;width:189px;height:175px;background:linear-gradient(180deg,#8a8a8a,#4a4a4a 60%,#2a2a2a)}
.product-name{top:1580px;width:230px;text-align:center;font-family:"Cinzel",serif;font-size:13px;color:var(--gold)}
.cta-photo{left:90px;top:1788px;width:1060px;height:305px;
  background:radial-gradient(ellipse at 50% 50%,#2d2822 0%,#1c1a16 45%,#0c0b09 80%,#000 100%)}
.cta-title{top:1886px;font-family:"Cinzel Decorative",serif;font-weight:700;font-size:31px;line-height:41px;color:var(--gold)}
.footer{left:0;top:2250px;width:1200px;height:302px;background:var(--footer)}
.footer-claim{left:130px;top:2345px;font-family:"Cinzel",serif;font-size:28px;line-height:36px;color:var(--gold)}
.footer-head{font-family:"Cinzel",serif;font-size:15px;color:var(--gold)}
.footer-text{font-family:"Cinzel",serif;font-size:14px;line-height:17px;color:var(--gold)}
.footer-rule{left:130px;top:2482px;width:938px;height:1px;background:#3b3a3d}
.footer-nav{top:2513px;left:153px;display:flex;gap:35px;font-family:"Cinzel",serif;font-size:11.5px;color:var(--gold)}
.copyright{top:2515px;right:134px;font-size:9px;color:#ddd}
</style>
</head>
<body>

<div class="abs topbar" style="left:130px">
  <svg viewBox="0 0 10 10"><circle cx="5" cy="5" r="4.2" fill="none" stroke="#e8e0d0" stroke-width=".9"/><path d="M5 2.6V5l1.6 1" fill="none" stroke="#e8e0d0" stroke-width=".9"/></svg>
  Mon - Fri 8:00 - 18:00 / Sunday 8:00 - 14:00
</div>
<div class="abs topbar" style="right:136px">
  <svg viewBox="0 0 10 10"><path d="M2.2 1l1.6 2-1 1.1c.6 1.3 1.6 2.3 2.9 2.9l1.1-1 2 1.6-.9 1.4C5 8.8 1.2 5 1 1.9z" fill="#e8e0d0"/></svg>
  0176/50938214
</div>

<div class="abs hero-photo" role="img" aria-label="Foto eines Blumenstraußes mit Rosen und Nelken in Pfirsich- und Rottönen"></div>

<svg class="abs frame" width="1200" height="200" viewBox="0 0 1200 200" aria-hidden="true">
  <path d="M140 165 C175 100 260 88 345 86 L368 58 Q373 52 382 52 L565 49 M635 49 L818 52 Q827 52 832 58 L855 86 C940 88 1025 100 1060 165" fill="none" stroke="#b89a62" stroke-width="1.2"/>
</svg>
<div class="abs brand"><span class="brand-dot"></span>Nurelan-Bestattung</div>

<nav class="abs nav">
  <a class="active" href="#">HOME</a>
  <a href="#">SERVICES</a>
  <a href="#">MEMORIALS</a>
  <a href="#">PAGES</a>
  <a href="#">CONTACTS</a>
</nav>

<h1 class="abs center hero-title">BESTATTUNGEN<br>DEUTSCHLANDWEIT<span class="gap"></span>ÜBERFÜHRUNGEN WELTWEIT</h1>
<a class="abs btn" href="#" style="left:545px;top:323px;width:108px;height:34px">Get In Touch</a>

<div class="abs service-card" style="left:248px">
  <h3>Bestattung<br>Leistungen</h3>
  <div class="bar">More Info</div>
  <div class="art" role="img" aria-label="Illustration von Rosen"></div>
</div>
<div class="abs service-card" style="left:498px">
  <h3>Grabsteine<br>Leistungen</h3>
  <div class="bar">More Info</div>
  <div class="art" role="img" aria-label="Illustration eines Grabsteins"></div>
</div>
<div class="abs service-card" style="left:750px">
  <h3>Grabpflege<br>Leistungen</h3>
  <div class="bar">More Info</div>
  <div class="art" role="img" aria-label="Illustration einer Grablaterne mit Blumen"></div>
</div>

<h2 class="abs about-title">Wir helfen Familien,<br>den letzten Abschied<br>zu nehmen</h2>
<p class="abs about-text">Wir wissen Ihr Vertrauen sehr zu schätzen. Unsere Kunden wählen uns und unsere Produkte, weil sie wissen, dass wir die Besten sind.</p>
<p class="abs hours" style="top:814px">MON-FRI: 9 AM – 22 PM</p>
<p class="abs hours" style="top:838px">SATURDAY: 9 AM – 20 PM</p>
<a class="abs btn-outline" href="#" style="left:264px;top:884px;width:108px;height:35px">About Us</a>

<div class="abs photo-arch" role="img" aria-label="Foto eines verzierten Moscheebogens im warmen Gegenlicht"></div>
<div class="abs photo-people" role="img" aria-label="Foto einer tröstenden Hand auf der Schulter einer trauernden Person"></div>

<p class="abs center eyebrow" style="top:1027px">Referenzen</p>
<h2 class="abs center section-title" style="top:1048px">Was unsere Familien sagen</h2>
<p class="abs center" style="top:1080px;font-family:'Cinzel',serif;font-size:20px;line-height:20px">”</p>
<p class="abs center quote">When it comes to immediate problem solving with such delicate and sometimes<br>terrifying circumstances, you know you have Sakina Dienst to fully trust and rely on.<br>Thank you for your impeccable work!</p>
<div class="abs" style="left:582px;top:1181px;width:36px;height:1px;background:var(--line)"></div>
<p class="abs center" style="top:1194px;font-size:11px;color:#eee">KARIM ESSER</p>
<p class="abs center" style="top:1209px;font-size:10px;color:#eee">Manager</p>

<p class="abs center eyebrow" style="top:1301px">Unser Laden</p>
<h2 class="abs center section-title" style="top:1322px">Unsere Produkte</h2>

<div class="abs product-img" style="left:166px" role="img" aria-label="Foto eines Grabsteins in Herzform mit Engelsrelief"></div>
<div class="abs product-img" style="left:392px" role="img" aria-label="Foto einer Grabanlage mit Herzstein und Blumen"></div>
<div class="abs product-img" style="left:618px" role="img" aria-label="Foto einer Grabanlage mit Minarett-Säulen"></div>
<div class="abs product-img" style="left:844px" role="img" aria-label="Foto eines zweiteiligen Grabsteins in Herzform"></div>
<p class="abs product-name" style="left:146px">White Casket Adornment</p>
<p class="abs product-name" style="left:372px">Mixed Flower Bouquet</p>
<p class="abs product-name" style="left:598px">Miniature Adornment</p>
<p class="abs product-name" style="left:824px">Rose and Freesia Posy</p>
<a class="abs btn" href="#" style="left:545px;top:1637px;width:108px;height:34px">View All</a>

<div class="abs cta-photo" role="img" aria-label="Dunkles Blumenarrangement mit Rosen, Sukkulenten und Gräsern"></div>
<p class="abs center eyebrow" style="top:1860px">Start Planning</p>
<h2 class="abs center cta-title">MÖCHTEN SIE EINEN GRABSTEIN<br>FÜR IHRE LIEBEN KAUFEN</h2>
<a class="abs btn" href="#" style="left:545px;top:2006px;width:108px;height:34px">Kontact Us</a>

<footer class="abs footer"></footer>
<p class="abs footer-claim">Wir organisieren &amp;<br>gestalten Zeremonien.</p>
<h3 class="abs footer-head" style="left:626px;top:2316px">Address</h3>
<p class="abs footer-text" style="left:626px;top:2353px">Germany —<br>12 Lindenweg, Büro 3<br>Berlin, DE 10115</p>
<h3 class="abs footer-head" style="left:871px;top:2316px">Say Hello</h3>
<p class="abs footer-text" style="left:871px;top:2353px">E-Mail: info@nurelan-bestattung.eu</p>
<p class="abs footer-text" style="left:871px;top:2388px">Tel.: 0176/50938214</p>
<div class="abs footer-rule"></div>
<nav class="abs footer-nav">
  <span>Home</span><span>Our Services</span><span>Our Pricing</span><span>Shop</span><span>Contact Us</span>
</nav>
<p class="abs copyright">Copyright Nurelan-Bestattung.eu © 2021</p>

</body>
</html>
```